The Maple Sprout Clinic needs a Letterhead

We are a bilingual pediatric clinic located in Montreal, Canada.

Our english name is Maple Sprout Clinic
Our french name is Clinique du petit ruisseau

We offer complete care for children including general pediatric care, pediatric specialist care such as Ear, Nose and Throat, Urology, Neurology and Adolescent Medicine. We also have paramedical specialists such as psychologists, social workers, occupational therapists, speech and language pathologists.

The letterhead must use and be harmonious with our new logo. See Design #4923293. We need two types of letterhead. One for a the Logo and both english and french names on the top and the second with the list of current staff on the left. I have uploaded two old examples for you to see. Thanks and good luck.

Font styles to use
Sans Serif

Colors
3176b5
9d9d9d

Requirements
Must have
• Include our logo.
Nice to have
• Most of our printing is done in black and white. So a grayscale design is fine.
I have included a color and grayscale versions of our logo.

We prefer clean modern designs.

```html
<!DOCTYPE html>
<html lang="en">
<head>
<meta charset="utf-8">
<title>Maple Sprout Clinic – Letterhead</title>
<link href="https://fonts.googleapis.com/css2?family=Source+Sans+3:wght@400;600;700&display=swap" rel="stylesheet">
<style>
  :root {
    --backdrop: #d9d9d9;
    --paper-top: #ffffff;
    --paper-bottom: #eeeeef;
    --sidebar: #e6e6e6;
    --brand: #5b67ab;
    --accent: #3b7f96;
    --ink: #333333;
    --watermark: #e9eaee;
    --edge: #2a2a2a;
  }
  * { box-sizing: border-box; margin: 0; padding: 0; }
  html, body { width: 1200px; height: 774px; overflow: hidden; }
  body {
    background: var(--backdrop);
    font-family: "Source Sans 3", Arial, sans-serif;
    color: var(--ink);
    position: relative;
  }
  .sheet {
    position: absolute;
    top: 18px;
    width: 565px;
    height: 730px;
    background: linear-gradient(180deg, var(--paper-top) 0%, var(--paper-top) 45%, var(--paper-bottom) 100%);
    border-right: 2px solid var(--edge);
    border-bottom: 2px solid var(--edge);
    box-shadow: 2px 2px 4px rgba(0,0,0,.35);
  }
  .sheet--staff { left: 20px; }
  .sheet--plain { left: 601px; }
  .sidebar {
    position: absolute; left: 0; top: 0; bottom: 0;
    width: 133px; background: var(--sidebar);
  }
  .masthead {
    position: absolute; top: 14px; left: 133px; right: 0;
    display: flex; justify-content: center; align-items: center; gap: 12px;
    color: var(--brand); font-size: 18px; line-height: 20px;
  }
  .masthead__fr { text-align: right; }
  .masthead__en { text-align: left; }
  .masthead__dot { width: 52px; height: 52px; border-radius: 50%; background: var(--brand); }
  .watermark {
    position: absolute; left: 217px; top: 258px;
    width: 260px; height: 216px; border-radius: 50%;
    background: var(--watermark);
  }
  .address { position: absolute; left: 13px; top: 115px; font-size: 10.5px; line-height: 13px; }
  .phones { position: absolute; left: 13px; top: 178px; font-size: 10.5px; line-height: 17px; }
  .phones li, .footer__line { list-style: none; display: flex; align-items: center; gap: 4px; }
  .icon { width: 10px; height: 10px; fill: var(--brand); }
  .staff { position: absolute; left: 13px; top: 222px; width: 118px; }
  .staff__group { margin-bottom: 9px; }
  .staff__fr { color: var(--brand); font-weight: 700; font-size: 10.5px; line-height: 12px; }
  .staff__en { color: var(--brand); font-weight: 700; font-size: 7.5px; line-height: 10px; }
  .staff__names { list-style: none; font-size: 7.8px; line-height: 11px; }
  .staff__names--spaced { margin-top: 7px; }
  .sidebar__phone { position: absolute; left: 12px; bottom: 14px; font-size: 12px; display: flex; gap: 4px; align-items: center; }
  .sidebar__phone .icon { width: 12px; height: 12px; }
  .footer {
    position: absolute; left: 133px; right: 0; bottom: 10px;
    display: flex; flex-direction: column; align-items: center;
    font-size: 10.5px; line-height: 17px;
  }
</style>
</head>
<body>

<svg width="0" height="0" style="position:absolute">
  <defs>
    <symbol id="icon-phone" viewBox="0 0 24 24"><path d="M12 1a11 11 0 1 0 0 22 11 11 0 0 0 0-22zm0 2a9 9 0 1 1 0 18 9 9 0 0 1 0-18zm-3.2 3.5c-.6 0-1.6 1-1.6 2.4 0 3.6 4.4 8.6 8.2 8.6 1.2 0 2-.9 2-1.4l-2.3-1.7-1.2 1c-1.5-.6-3-2.4-3.4-3.8l1-1.1z"/></symbol>
    <symbol id="icon-car" viewBox="0 0 24 24"><path d="M5 10l2-5h10l2 5h1.5v7H19v2h-3v-2H8v2H5v-2H3.5v-7zm3-3.3L6.9 10h10.2L16 6.7zM6.5 12a1.3 1.3 0 1 0 0 2.6 1.3 1.3 0 0 0 0-2.6zm11 0a1.3 1.3 0 1 0 0 2.6 1.3 1.3 0 0 0 0-2.6z"/></symbol>
  </defs>
</svg>

<section class="sheet sheet--staff" aria-label="Letterhead with staff list">
  <aside class="sidebar">
    <p class="address">2250 rue des Érables<br>Suite 100<br>Pointe-Claire, Qc<br>H9R 3K2</p>
    <ul class="phones">
      <li><svg class="icon"><use href="#icon-phone"/></svg>(514) 555-0142</li>
      <li><svg class="icon"><use href="#icon-car"/></svg>(514) 555-0187</li>
    </ul>
    <div class="staff">
      <div class="staff__group">
        <p class="staff__fr">Pédiatres</p><p class="staff__en">Pediatricians</p>
        <ul class="staff__names staff__names--spaced">
          <li>H. Bellamy</li><li>J. Fortin</li><li>R. Lindqvist</li><li>D. Paquet</li><li>N. Tremblay</li><li>M. Carver</li><li>D. Moreau</li>
        </ul>
      </div>
      <div class="staff__group">
        <p class="staff__fr">Neurologue</p><p class="staff__en">Neurologist</p>
        <ul class="staff__names"><li>M. Hartley</li></ul>
      </div>
      <div class="staff__group">
        <p class="staff__fr">O.R.L.</p><p class="staff__en">E.N.T.</p>
        <ul class="staff__names"><li>T. Nadeau</li></ul>
      </div>
      <div class="staff__group">
        <p class="staff__fr">Urologue</p><p class="staff__en">Urologist</p>
        <ul class="staff__names"><li>R. Okafor</li></ul>
      </div>
      <div class="staff__group">
        <p class="staff__fr">Psychologues</p><p class="staff__en">Psychologists</p>
        <ul class="staff__names"><li>H. Gagnon</li><li>A. Leblanc</li></ul>
      </div>
      <div class="staff__group">
        <p class="staff__fr">Travailleuse social</p><p class="staff__en">Social worker</p>
        <ul class="staff__names"><li>S. Dubois</li></ul>
      </div>
      <div class="staff__group">
        <p class="staff__fr">Gerante</p><p class="staff__en">Manager</p>
        <ul class="staff__names"><li>C. Rinaldi</li></ul>
      </div>
    </div>
    <p class="sidebar__phone"><svg class="icon"><use href="#icon-phone"/></svg>(514) 555-0142</p>
  </aside>
  <header class="masthead">
    <p class="masthead__fr">Clinique<br>du petit<br>ruisseau</p>
    <span class="masthead__dot"></span>
    <p class="masthead__en">Maple<br>Sprout<br>Clinic</p>
  </header>
  <div class="watermark"></div>
  <footer class="footer">
    <p class="footer__line"><svg class="icon"><use href="#icon-car"/></svg>(514) 555-0187</p>
    <p>2250 rue des Érables, Suite 100, Pointe-Claire, Qc, H9R 3K2</p>
  </footer>
</section>

<section class="sheet sheet--plain" aria-label="Letterhead without staff list">
  <aside class="sidebar">
    <p class="sidebar__phone"><svg class="icon"><use href="#icon-phone"/></svg>(514) 555-0142</p>
  </aside>
  <header class="masthead">
    <p class="masthead__fr">Clinique<br>du petit<br>ruisseau</p>
    <span class="masthead__dot"></span>
    <p class="masthead__en">Maple<br>Sprout<br>Clinic</p>
  </header>
  <div class="watermark"></div>
  <footer class="footer">
    <p class="footer__line"><svg class="icon"><use href="#icon-car"/></svg>(514) 555-0187</p>
    <p>2250 rue des Érables, Suite 100, Pointe-Claire, Qc, H9R 3K2</p>
  </footer>
</section>

</body>
</html>
```